"Tidy Nest " A Pest Control Company needs Postcard Campaign Design

Design a visually engaging postcard for " Tidy Nest ", a new pest control company. The postcard should capture attention with bold and vibrant imagery, showcasing various pests and emphasizing our comprehensive pest control services.
This will be mailed as post Card in hope to capture new leads from residents who experience pest difficulties and wants them removed

Target Market(s)

Residential Homes

Industry/Entity Type

Pest Control

Font styles to use
Serif
Sans Serif

Colors
00AB8E
00BBA5
67D7C9
C6EFE9
E9F9F6

Requirements
Must have
• Offer: " $49 Service fee ( Small letters ) with any subscription " * SEE ATTACHMENT for Core Fundamentals - Messaging Choose about 4 and the post card size "
Nice to have
• * SEE ATTACHMENT " Picture of a pest control technician (Make sure he is branded with our logo) .

```html
<!DOCTYPE html>
<html lang="en">
<head>
<meta charset="UTF-8">
<title>Tidy Nest Postcard</title>
<link href="https://fonts.googleapis.com/css2?family=Jost:ital,wght@0,400;0,500;0,600;0,700;1,600&display=swap" rel="stylesheet">
<style>
  :root {
    --stage: #cfcfcf;
    --paper: #ffffff;
    --green: #3ab54a;
    --green-soft: #dcf1de;
    --ink: #1b1b1b;
    --navy: #1d2b48;
    --rule: #8a8a8a;
    --photo-light: #f4f5f5;
    --photo-mid: #e3e6e6;
  }
  * { margin: 0; padding: 0; box-sizing: border-box; }
  html, body { width: 970px; height: 1200px; overflow: hidden; }
  body {
    background: var(--stage);
    font-family: "Jost", "Century Gothic", sans-serif;
    color: var(--ink);
    position: relative;
  }
  .postcard {
    position: absolute;
    left: 85px;
    width: 800px;
    height: 533px;
    background: var(--paper);
    overflow: hidden;
    box-shadow: 0 2px 6px rgba(0,0,0,0.25);
  }
  .postcard--front { top: 51px; }
  .postcard--back { top: 618px; }

  .layer { position: absolute; }
  .shapes { position: absolute; inset: 0; width: 800px; height: 533px; }

  .technician-photo {
    position: absolute;
    left: 420px; top: 0;
    width: 380px; height: 533px;
    background: linear-gradient(100deg, rgba(255,255,255,0) 0%, var(--photo-light) 25%, var(--photo-mid) 70%, var(--photo-light) 100%);
  }

  .brand-name {
    position: absolute;
    left: 595px; top: 92px;
    width: 170px;
    text-align: center;
    font-size: 34px;
    font-weight: 700;
    line-height: 1;
    color: var(--navy);
  }

  .section-title {
    font-size: 13px;
    font-weight: 700;
    color: var(--green);
    text-transform: uppercase;
    letter-spacing: 0.2px;
  }
  .key-elements { left: 38px; top: 32px; width: 520px; font-size: 11px; line-height: 15.6px; }
  .key-elements .section-title { line-height: 18px; }
  .key-elements h3 { font-size: 11px; font-style: italic; font-weight: 600; }
  .key-elements p { font-weight: 400; }

  .problems { left: 38px; top: 170px; width: 560px; }
  .problems .section-title { margin-bottom: 3px; }
  .problems ol, .usps ol { list-style: none; }
  .problems li { font-size: 11px; line-height: 18.6px; }

  .usps { left: 38px; top: 351px; width: 400px; color: #fff; }
  .usps .section-title { color: #fff; margin-bottom: 4px; }
  .usps li { font-size: 11px; line-height: 18.4px; font-weight: 500; }

  .offer {
    left: 540px; top: 333px; width: 140px;
    text-align: center; font-size: 11px; line-height: 14px;
  }
  .offer .price { font-size: 20px; font-weight: 700; }
  .offer-note {
    left: 548px; top: 388px; width: 140px;
    text-align: center; font-size: 11px; line-height: 15px;
  }

  .uvp { left: 38px; top: 74px; width: 512px; }
  .uvp h2, .subscriber-reasons h2 {
    font-size: 13px; font-weight: 700; text-transform: uppercase; line-height: 18px;
  }
  .uvp p { font-size: 12.5px; line-height: 17.6px; }

  .subscriber-reasons { left: 38px; top: 285px; width: 520px; }
  .subscriber-reasons ol { list-style: none; }
  .subscriber-reasons li {
    position: relative;
    padding-left: 26px;
    font-size: 12.5px;
    line-height: 17.6px;
  }
  .subscriber-reasons .num { position: absolute; left: 0; }

  .stamp-box {
    left: 657px; top: 46px; width: 96px; height: 113px;
    border: 1px solid var(--rule);
  }
  .address-line {
    left: 559px; width: 194px; height: 1px; background: var(--rule);
  }
</style>
</head>
<body>

<section class="postcard postcard--front">
  <div class="technician-photo" role="img" aria-label="Photo of a pest control technician in a white protective suit spraying a room"></div>

  <svg class="shapes" viewBox="0 0 800 533" aria-hidden="true">
    <path d="M0 200 C 120 185, 300 190, 380 215 L 460 533 L 0 533 Z" fill="var(--green-soft)"/>
    <path d="M0 318 C 140 300, 330 300, 420 325 C 440 400, 445 470, 466 533 L 0 533 Z" fill="var(--green)"/>
    <path d="M460 382 L 545 382 L 636 470 L 776 382 L 636 505 Z" fill="var(--green)" opacity="0.9"/>
  </svg>

  <div class="brand-name">Tidy Nest</div>

  <div class="layer key-elements">
    <h2 class="section-title">Key Elements to Emphasize</h2>
    <h3>1. Thorough, Fast Cleanup &amp; Removal</h3>
    <p>We ensure your home is back to normal quickly, without the worry of Pests .</p>
    <h3>2. Assured Elimination</h3>
    <p>Our professional expertise guarantees all traces of rodents are gone, providing lasting comfort.</p>
    <h3>3. Guaranteed Prevention</h3>
    <p>Our industry-leading methods and warranty ensure you never have to deal with Pests &nbsp;again.</p>
  </div>

  <div class="layer problems">
    <h2 class="section-title">Main Problems Addressed</h2>
    <ol>
      <li>1. Unwanted, Unsanitary Presence: Pests &nbsp;are completely removed.</li>
      <li>2. Discomfort, Anxiety, and Violation of Personal Space: We restore your peace of mind.</li>
      <li>3. Perception of Dirtiness &amp; Disorder: Our thorough cleanup restores cleanliness.</li>
      <li>4. Disruption of Safety &amp; Sanctity: We secure your home against future invasions.</li>
      <li>5. Fear of Encountering Rodents Unexpectedly: Our prevention methods provide lasting protection.</li>
    </ol>
  </div>

  <div class="layer usps">
    <h2 class="section-title">Unique Selling Points (USPS)</h2>
    <ol>
      <li>1. Bay Area Local</li>
      <li>2. Family-owned and operated</li>
      <li>3. Professional experts and credibility</li>
      <li>4. Eco-friendly treatments</li>
      <li>5. Industry-leading warranty</li>
      <li>6. Extremely strong attention-to-detail, diligence, and honesty</li>
      <li>7. We do the job once, and right</li>
    </ol>
  </div>

  <div class="layer offer">
    <span class="price">$49</span> Service fee<br>with any subscription
  </div>
  <div class="layer offer-note">* SEE ATTACHMENT for Core Fundamentals</div>
</section>

<section class="postcard postcard--back">
  <svg class="shapes" viewBox="0 0 800 533" aria-hidden="true">
    <path d="M0 0 L 60 0 L 300 533 L 240 533 Z" fill="var(--green-soft)"/>
  </svg>

  <div class="layer uvp">
    <h2>Unique Value Proposition (UVP)</h2>
    <p>Tidy Nest stands out as the gold standard in Pest Control , offering comprehensive and reliable solutions for the entire Bay Area. Our family-owned, local business ensures fast, thorough cleanup, assured elimination, and long-term prevention using advanced, cutting-edge tactics and eco-friendly methods. We provide unmatched service and peace of mind. Our trusted, reliable approach guarantees exceptional customer satisfaction and a Pest-free home, making us the Bay Area's #1 choice for Pest Control.</p>
  </div>

  <div class="layer subscriber-reasons">
    <h2>Enhanced List of Reasons to Stay on as an Email Subscriber:</h2>
    <ol>
      <li><span class="num">1.</span>Educational Content: Subscribers receive regular tips and advice on maintaining a rodent-free home, including spotting early signs of infestations and preventative measures.</li>
      <li><span class="num">2.</span>Exclusive Offers &amp; Special Discounts: Subscribers benefit from special promotions, referral incentives, and discounts on extended warranties.</li>
      <li><span class="num">3.</span>Updates - New Services, Technology, Tactics &amp; Strategies: Subscribers are kept informed about new services, technology improvements, techniques, and success stories.</li>
      <li><span class="num">4.</span>Personalized Insights and Assessments: Providing tailored advice and tips based on subscribers' specific situations, home types, or seasonal needs.</li>
    </ol>
  </div>

  <div class="layer stamp-box"></div>
  <div class="layer address-line" style="top: 330px;"></div>
  <div class="layer address-line" style="top: 379px;"></div>
  <div class="layer address-line" style="top: 428px;"></div>
</section>

</body>
</html>
```